Sales Flyer Advertising Aircraft Sales & Acquisitions

Looking for very professional flyer that can also be converted and sent as an email. Something simple but very high end. Maybe a line on there about taking advantage of 80% tax deduction before it drops this year. Don’t want it to seem too salesy but also catch the eye and get the message across. My website is www.quillonaerospan.com to give you an idea. It is in the process of being reworked but it’s something to go off of.

```html
<!DOCTYPE html>
<html lang="en">
<head>
<meta charset="UTF-8">
<title>Quillon Aerospan Services — Sales Flyer</title>
<link href="https://fonts.googleapis.com/css2?family=Inter:ital,wght@0,400;0,600;0,700;1,400;1,700&family=Inter+Tight:wght@600&display=swap" rel="stylesheet">
<style>
  :root {
    --backdrop: #6e6e6e;
    --paper: #d3d4d9;
    --ink: #3b3c42;
    --navy: #2d3040;
    --white-soft: rgba(255,255,255,0.9);
    --label-bg: #e9eaee;
  }
  * { margin: 0; padding: 0; box-sizing: border-box; }
  html, body { width: 925px; height: 1200px; overflow: hidden; background: var(--backdrop); }
  body { font-family: "Inter", Helvetica, Arial, sans-serif; }

  .flyer {
    position: absolute; left: 82px; top: 22px;
    width: 752px; height: 1138px;
    background: var(--paper);
    overflow: hidden;
  }
  .photo { position: absolute; }
  .photo-aircraft {
    left: 0; top: 440px; width: 752px; height: 236px;
    background: linear-gradient(180deg, rgba(200,201,207,0) 0%, #c0c1c7 40%, #b2b3b9 65%, rgba(200,201,207,0) 100%);
  }
  .photo-engine {
    left: 0; top: 502px; width: 299px; height: 501px;
    background: radial-gradient(circle at 18% 50%, #88898f 0%, #a4a5ab 40%, #bbbcc1 80%, #c5c6cb 100%);
  }

  .stat-number {
    position: absolute; left: 42px; top: 10px;
    font-family: "Inter Tight", "Inter", Helvetica, sans-serif;
    font-size: 420px; font-weight: 600; letter-spacing: -25px;
    color: var(--ink); line-height: 1;
  }
  .stat-percent {
    position: absolute; left: 462px; top: 244px;
    font-size: 140px; font-weight: 400; color: var(--white-soft); line-height: 1;
  }
  .stat-label {
    position: absolute; left: 57px; top: 403px;
    width: 384px; height: 25px; background: var(--label-bg);
    font-size: 16px; font-style: italic; color: var(--navy);
    line-height: 25px; padding-left: 20px; letter-spacing: 0.3px;
  }

  .vision-word {
    position: absolute; left: 511px; top: 222px;
    width: 345px; height: 92px;
    transform-origin: center; transform: rotate(90deg) scaleY(-1);
    font-size: 92px; font-weight: 600; color: var(--white-soft);
    line-height: 92px; letter-spacing: 12px; text-align: center; white-space: nowrap;
  }
  .vision-statement {
    position: absolute; right: 118px; top: 108px; width: 130px;
    text-align: right; font-size: 12px; font-style: italic;
    line-height: 16px; color: var(--navy);
  }

  .headline {
    position: absolute; left: 67px; top: 584px;
    color: #fff; font-size: 46px; line-height: 57px;
  }
  .headline .strong { font-weight: 700; }
  .headline .soft { font-weight: 400; font-style: italic; }

  .services { position: absolute; right: 51px; top: 742px; text-align: right; color: var(--navy); }
  .services-title { font-size: 36px; line-height: 40px; font-weight: 700; font-style: italic; margin-bottom: 7px; }
  .services-list { list-style: none; font-size: 17px; font-style: italic; line-height: 28px; padding-right: 4px; }
  .services-list li::after { content: "\2022"; font-style: normal; margin-left: 8px; }

  .brand {
    position: absolute; right: 55px; top: 1018px;
    display: flex; align-items: center; gap: 9px;
  }
  .brand-square { width: 13px; height: 13px; background: #000; }
  .brand-name { font-size: 15px; font-weight: 700; color: #000; letter-spacing: 0.4px; }

  .website {
    position: absolute; left: 64px; top: 1041px;
    font-size: 18px; font-weight: 700; color: var(--ink);
  }
</style>
</head>
<body>
  <main class="flyer">
    <div class="photo photo-aircraft" role="img" aria-label="Photograph of a jet airliner on approach with landing gear down and lights on"></div>
    <div class="photo photo-engine" role="img" aria-label="Close-up photograph of a jet engine fan"></div>

    <div class="stat-number">80</div>
    <div class="stat-percent">%</div>
    <div class="stat-label">tax deduction before it drops this year</div>

    <div class="vision-word">Vision</div>
    <p class="vision-statement">To provide clients<br>with a positive<br>experience while<br>redefining industry<br>standards for<br>aircraft sales.</p>

    <h1 class="headline">
      <span class="strong">Soaring</span><br>
      <span class="soft">for</span><br>
      <span class="strong">Excellence.</span>
    </h1>

    <section class="services">
      <h2 class="services-title">Services</h2>
      <ul class="services-list">
        <li>Aircraft Sales</li>
        <li>Aircraft Acquisitions</li>
        <li>Pre-Purchase Inspections</li>
        <li>Ferry Pilot Services</li>
        <li>Aircraft Management</li>
      </ul>
    </section>

    <div class="brand">
      <span class="brand-square"></span>
      <span class="brand-name">QUILLON AEROSPAN SERVICES</span>
    </div>

    <div class="website">www.quillonaerospan.com</div>
  </main>
</body>
</html>
```